TRESSLY FACEBOOK DESIGN

I need new design for facebook https://www.facebook.com/tresslyitalia.
Our Businnes is Hair care , hair replacement , hair transplant . hair regrowth . i NEED MEDICAL AND PROFESSIONAL DESIGN. I NEED ALSO RESPONSIVE DESIGN

Target Market(s)

Consumers

Industry/Entity Type

MEDICAL AND COSMETICS

Colors
0054AA
0677BA
7BADD7
CADEEF
E8F1F8

Requirements
Must have
• MEDICAL
Nice to have
• RESPONSIVE DESIGN

```html
<!DOCTYPE html>
<html lang="it">
<head>
<meta charset="utf-8">
<title>Tressly – Facebook Post</title>
<link rel="stylesheet" href="https://fonts.googleapis.com/css2?family=Montserrat:wght@600;700;800&family=Open+Sans:wght@400;600&display=swap">
<style>
  :root {
    --blue-deep: #0054AA;
    --blue-mid: #0677BA;
    --blue-soft: #7BADD7;
    --blue-pale: #CADEEF;
    --blue-mist: #E8F1F8;
    --white: #FFFFFF;
    --ink: #1C1C1C;
  }
  * { margin: 0; padding: 0; box-sizing: border-box; }
  html, body {
    width: 1200px;
    height: 700px;
    overflow: hidden;
    background: var(--blue-mist);
  }
  .canvas {
    width: 1200px;
    height: 700px;
    display: flex;
    align-items: center;
    justify-content: center;
  }
  .post {
    width: 660px;
    height: 660px;
    display: block;
    box-shadow: 0 10px 30px rgba(0, 40, 90, 0.18);
  }
  .brand-name { font-family: "Montserrat", sans-serif; font-weight: 700; font-size: 62px; fill: var(--blue-mid); }
  .brand-tagline { font-family: "Open Sans", sans-serif; font-weight: 600; font-size: 15px; fill: var(--blue-mid); letter-spacing: 0.3px; }
  .headline-main { font-family: "Montserrat", sans-serif; font-weight: 800; font-size: 60px; fill: var(--blue-deep); }
  .headline-sub { font-family: "Montserrat", sans-serif; font-weight: 700; font-size: 53px; fill: var(--blue-mid); }
  .section-title { font-family: "Montserrat", sans-serif; font-weight: 800; font-size: 39px; fill: var(--blue-deep); }
  .service-label { font-family: "Open Sans", sans-serif; font-weight: 400; font-size: 33px; fill: var(--ink); letter-spacing: 0.5px; }
  .cta-label { font-family: "Montserrat", sans-serif; font-weight: 800; font-size: 38px; fill: var(--blue-deep); }
  .web-address { font-family: "Montserrat", sans-serif; font-weight: 600; font-size: 29px; fill: var(--white); }
</style>
</head>
<body>
<main class="canvas">
  <svg class="post" viewBox="0 0 1096 1096" xmlns="http://www.w3.org/2000/svg">
    <defs>
      <clipPath id="post-frame"><rect width="1096" height="1096"/></clipPath>
      <linearGradient id="portrait-tone" x1="0" y1="0" x2="1" y2="1">
        <stop offset="0" stop-color="#e4e4e4"/>
        <stop offset="0.5" stop-color="#9a9a9a"/>
        <stop offset="1" stop-color="#4a4a4a"/>
      </linearGradient>
      <filter id="icon-shadow" x="-30%" y="-30%" width="160%" height="160%">
        <feDropShadow dx="0" dy="2" stdDeviation="2" flood-color="#000" flood-opacity="0.25"/>
      </filter>
    </defs>

    <g clip-path="url(#post-frame)">
      <rect class="post-background" width="1096" height="1096" fill="var(--white)"/>

      <!-- decorative circles -->
      <circle class="accent-dot" cx="524" cy="608" r="100" fill="var(--blue-pale)"/>
      <path class="accent-arc" d="M541,158 A370,370 0 0 0 578,581" fill="none" stroke="var(--blue-mid)" stroke-width="3"/>
      <path class="accent-arc" d="M995,28 Q1060,55 1096,95" fill="none" stroke="var(--blue-mid)" stroke-width="3"/>
      <circle class="portrait-ring" cx="861" cy="343" r="305" fill="none" stroke="var(--blue-deep)" stroke-width="55"/>

      <!-- portrait area -->
      <g class="portrait" role="img" aria-label="Black and white photo of a smiling woman with long dark hair combing it">
        <circle cx="861" cy="343" r="277" fill="url(#portrait-tone)"/>
        <rect x="640" y="343" width="456" height="600" fill="url(#portrait-tone)"/>
      </g>

      <!-- brand -->
      <g class="brand">
        <circle cx="58" cy="72" r="24" fill="var(--blue-mid)"/>
        <text class="brand-name" x="96" y="94">Tressly</text>
        <text class="brand-tagline" x="38" y="131">CURA E REINTEGRAZIONE DEI CAPELLI</text>
      </g>

      <!-- headline -->
      <text class="headline-main" x="28" y="298">LOREM IPSUM</text>
      <text class="headline-sub" x="28" y="350">DOLOR SIT AMET</text>

      <!-- services -->
      <text class="section-title" x="30" y="525">OUR BUSINNES</text>
      <rect class="section-rule" x="30" y="533" width="322" height="4" fill="var(--blue-mid)"/>

      <g class="service-item">
        <circle cx="61" cy="582" r="25" fill="var(--blue-deep)" stroke="var(--white)" stroke-width="4" filter="url(#icon-shadow)"/>
        <rect x="54" y="568" width="14" height="28" rx="3" fill="var(--white)"/>
        <circle cx="61" cy="586" r="3" fill="var(--blue-deep)"/>
        <text class="service-label" x="106" y="594">HAIR CARE</text>
      </g>
      <g class="service-item">
        <circle cx="61" cy="651" r="25" fill="var(--blue-deep)" stroke="var(--white)" stroke-width="4" filter="url(#icon-shadow)"/>
        <path d="M50,640 L61,662 L72,640 M61,662 L61,640" fill="none" stroke="var(--white)" stroke-width="3" stroke-linecap="round"/>
        <text class="service-label" x="106" y="663">HAIR REPLACEMENT</text>
      </g>
      <g class="service-item">
        <circle cx="61" cy="720" r="25" fill="var(--blue-deep)" stroke="var(--white)" stroke-width="4" filter="url(#icon-shadow)"/>
        <path d="M54,708 Q62,716 63,730" fill="none" stroke="var(--white)" stroke-width="3" stroke-linecap="round"/>
        <rect x="52" y="728" width="18" height="5" rx="2" fill="var(--white)"/>
        <text class="service-label" x="106" y="732">HAIR TRANSPLANT</text>
      </g>

      <!-- footer waves -->
      <path class="wave-accent" d="M0,838 C200,808 380,835 560,885 C760,940 950,905 1096,832 L1096,845 C950,918 760,952 560,898 C380,850 200,825 0,858 Z" fill="var(--blue-mid)"/>
      <path class="wave-band" d="M0,872 C200,834 380,855 560,908 C760,966 950,935 1096,862 L1096,1096 L0,1096 Z" fill="var(--blue-deep)"/>

      <!-- call to action -->
      <g class="cta-button">
        <rect x="31" y="991" width="300" height="65" rx="6" fill="var(--white)"/>
        <text class="cta-label" x="181" y="1037" text-anchor="middle">LEARN MORE</text>
      </g>
      <text class="web-address" x="1065" y="1053" text-anchor="end">WWW.LOREMIPSUM.COM</text>
    </g>
  </svg>
</main>
</body>
</html>
```